Web Site for Strategy and Technology Consulting Company

We are looking for a website design that engages potential customers to understand our services and contact us. In this contest, we are looking for a homepage design, but the winning designer will be favored for the design of some of the more complicated interior pages of the site. An additional contest (or contests) for these pages will be added soon.

PLATROM AND RESPONSIVE DESIGN
The site will be implemented in WordPress using the Elementor page builder.
We are looking for a design that will look good on phones are well as laptop browsers.

UPLOADED FILES INCLUDE:
1a A wireframe of the homepage we are looking for. The Uploaded PDF also includes a draft of the text proposed for the homepage. Designers are free to go beyond the wireframe, but all elements of the wireframe should be included.
1b A Word document with the draft text of the homepage.
2a-d The Corvalin logo. Two versions are included – a dark version which works well against a light background, and a light version which works well against a dark background.
3 The Corvalin color palette with HEX and RGB values. Designers are not limited to this palette, but colors should be complementary.
4 A draft of the homepage menu
5 Service sheets with information on the services we provide

MORE ABOUT CORVALIN
Corvalin is a consulting company focused on transforming businesses through software. Our tagline, “Transformation Delivered,” recognizes the gap business often have between business transformation and the software they end up with. By listening to our customers and understanding their vision and where they are, we help get our customers where they want to go.

We increase our capability by working with many consultants and partners, allowing us to provide our customers with the best people and the software that best suits them.

Industry/Entity Type

Consulting

Number of Pages Required

1 page

Font styles to use
Sans Serif

Requirements
Must have
• the content represented on the wireframe uploaded
Nice to have
• interactive features, such as roll-over icons that reveal additional information

```html
<!DOCTYPE html>
<html lang="en">
<head>
<meta charset="utf-8">
<title>Corvalin — Transformation Delivered</title>
<link rel="stylesheet" href="https://fonts.googleapis.com/css2?family=DM+Sans:wght@400;500;700&display=swap">
<style>
:root{
  --navy:#1d2a44;
  --navy-deep:#141d30;
  --blue:#2e6da4;
  --sky:#dcebfa;
  --gold:#e3b81c;
  --ink:#2c3a52;
  --muted:#5b6678;
  --footer:#4b5a77;
  --white:#ffffff;
}
*{box-sizing:border-box;margin:0;padding:0}
html,body{width:1200px;height:3495px;overflow:hidden}
body{font-family:'DM Sans',sans-serif;color:var(--ink);background:#fff;position:relative}
section,footer{position:absolute;left:0;width:1200px}
.abs{position:absolute}

/* hero */
.hero{top:0;height:704px;background:linear-gradient(100deg,#1c2c48 0%,#2a3d5c 45%,#3a4e6a 70%,#24344e 100%);color:#fff}
.hero-photo{position:absolute;inset:0;background:radial-gradient(ellipse at 78% 45%,rgba(70,140,170,.35),transparent 45%),radial-gradient(ellipse at 55% 35%,rgba(120,110,95,.35),transparent 40%),linear-gradient(90deg,rgba(20,32,56,.85) 0%,rgba(20,32,56,.45) 55%,rgba(20,32,56,.2) 100%)}
.brand{font-size:36px;font-weight:500;letter-spacing:-.5px;display:flex;align-items:center;gap:6px}
.brand::before{content:"";width:7px;height:7px;border-radius:50%;background:currentColor}
.nav{top:50px;left:563px;display:flex;gap:28px;font-size:12px;font-weight:700}
.nav span::after{content:" ⌄";font-size:11px}
.contact-btn{top:40px;left:980px;width:121px;height:34px;background:var(--blue);font-size:12px;font-weight:700;display:flex;align-items:center;justify-content:center}
.hero h1{top:160px;left:98px;font-size:54px;line-height:60px;font-weight:700}
.hero-lead{top:284px;left:98px;width:550px;font-size:14px;line-height:19px}
.checks{top:384px;left:98px;list-style:none;font-size:13px;font-weight:700}
.checks li{display:flex;gap:9px;margin-bottom:16px;line-height:19px}
.checks li::before{content:"✓";flex:none;width:13px;height:13px;margin-top:3px;border-radius:50%;background:var(--gold);color:var(--navy);font-size:9px;display:flex;align-items:center;justify-content:center}
.story-btn{top:559px;left:98px;width:193px;height:50px;background:var(--gold);color:var(--navy);font-size:18px;font-weight:500;display:flex;align-items:center;justify-content:center;gap:8px}

/* services */
.services{top:704px;height:629px;background:var(--sky)}
.services h2{top:76px;left:99px;font-size:35px;line-height:43px;font-weight:500;color:var(--navy)}
.services-intro{top:90px;left:448px;width:600px;font-size:15px;line-height:26px;color:var(--muted)}
.service{top:277px;height:248px;width:205px;padding:0 0 0 19px;color:var(--navy)}
.service + .service{border-left:1px solid #9fb0c4}
.service svg{display:block;height:50px}
.service h3{font-size:19px;line-height:24px;font-weight:500;margin-top:14px}
.service p{font-size:13px;line-height:19px;color:var(--muted);margin-top:14px;width:160px}
.service .more{position:absolute;top:210px;font-size:13px;color:var(--navy)}
.wordmark{font-size:25px;font-weight:500;color:var(--blue);line-height:28px;display:block}
.wordmark small{display:block;font-size:11px;color:var(--muted);line-height:11px}

/* people */
.people{top:1333px;height:978px;text-align:center}
.people h2{top:83px;width:100%;font-size:35px;font-weight:500;color:#3c4a66}
.people-intro{top:149px;left:120px;width:960px;font-size:15px;line-height:26px;color:var(--muted)}
.point{top:234px;display:flex;gap:12px;text-align:left;font-size:19px;line-height:26px;font-weight:500;color:var(--navy)}
.point b{flex:none;width:49px;height:49px;background:var(--gold);color:#fff;font-size:38px;display:flex;align-items:center;justify-content:center}
.map{top:357px;left:230px;width:745px;height:380px;background:radial-gradient(ellipse at 50% 50%,#f6e6d0 0%,#fbf2e6 60%,#fff 100%);border-radius:40%}
.pin{width:46px;height:46px;border-radius:50%;background:linear-gradient(#c9b6a3,#7e8ea3);border:3px solid #fff;box-shadow:0 2px 8px rgba(0,0,0,.2)}
.tag{top:363px;left:558px;background:var(--blue);color:#fff;font-size:12px;padding:4px 14px}
.people-note{top:808px;width:100%;font-size:15px;color:var(--muted)}
.team-btn{top:852px;left:489px;width:222px;height:51px;background:var(--gold);color:var(--navy);font-size:15px;font-weight:500;display:flex;align-items:center;justify-content:center}

/* testimonials */
.testimonials{top:2311px;height:543px;background:linear-gradient(90deg,#1e2638,#2a3347 50%,#1b2334);color:#fff;text-align:center}
.testimonials .eyebrow{top:114px;width:100%;font-size:15px;font-weight:500;color:var(--gold)}
.testimonials h2{top:144px;width:100%;font-size:34px;font-weight:700}
.avatar{top:234px;left:564px;width:72px;height:72px;border-radius:50%;background:linear-gradient(#d9d2c8,#8e99ab);border:3px solid #fff}
.quote{top:325px;left:280px;width:640px;font-size:13px;line-height:21px}
.author{top:402px;width:100%;font-size:12px;line-height:17px;font-weight:500;color:var(--blue)}
.author span{display:block;color:var(--gold);font-weight:400}
.dots{display:flex;gap:9px;justify-content:center}
.dots i{width:7px;height:7px;background:#fff;display:block}
.dots i.on{outline:2px solid var(--blue);outline-offset:2px}

/* technologies */
.tech{top:2854px;height:292px}
.tech .eyebrow{top:42px;left:99px;font-size:15px;color:var(--gold)}
.tech h2{top:76px;left:97px;font-size:34px;font-weight:500;color:var(--navy)}
.logos{top:156px;left:97px;width:1000px;display:flex;justify-content:space-between;align-items:center}
.logos span{display:flex;align-items:center;gap:8px;font-size:20px;font-weight:500;color:#4a5568}
.logos span::before{content:"";width:14px;height:14px;background:#9aa6b8;border-radius:50%}
.tech-dots{top:232px;left:580px;display:flex;gap:6px}
.tech-dots i{width:7px;height:7px;border-radius:50%;background:#9ab0d0;display:block}
.tech-dots i.on{background:var(--gold)}

/* footer */
footer{top:3146px;height:349px;background:var(--footer);color:#fff}
footer .brand{top:72px;left:101px;font-size:32px}
.footer-about{top:122px;left:101px;width:420px;font-size:13px;line-height:22px}
footer h4{font-size:18px;font-weight:700;margin-bottom:20px}
.footer-col{top:84px;font-size:14px;line-height:22px}
.email{border-bottom:1px solid #fff;padding-bottom:6px;display:inline-block}
.phone{font-size:17px;margin-top:16px}
.socials{display:flex;gap:10px;margin-top:20px}
.socials i{width:36px;height:36px;border:1px solid #fff;border-radius:50%;display:block}
.footer-links{top:298px;left:98px;font-size:13px}
.copyright{top:298px;left:812px;font-size:13px}
</style>
</head>
<body>

<section class="hero">
  <div class="hero-photo" role="img" aria-label="Photo of consultants reviewing a dashboard on a monitor in an office"></div>
  <div class="abs brand" style="top:30px;left:106px">Corvalin</div>
  <nav class="abs nav"><span>ABOUT US</span><span>SERVICES</span><span>INSIGHTS</span><span>JOIN US</span></nav>
  <div class="abs contact-btn">CONTACT US</div>
  <h1 class="abs">Transformation<br>Delivered.</h1>
  <p class="abs hero-lead">We do more for our customers than implement software. We listen. We work to understand where they are in their transformation journey and where they want to go. We partner with them to clear the roadblocks that stand in their way, ensuring they reach their destination.</p>
  <ul class="abs checks">
    <li>Focus on business value, with an emphasis on delivering value quickly.</li>
    <li>Meet our customers where they are without backing them up to<br>the beginning of their journey.</li>
    <li>Provide a wide range of services, from strategy to product support.</li>
    <li>Commit to our customer’s long-term success.</li>
  </ul>
  <div class="abs story-btn">OUR STORY
    <svg width="22" height="22" viewBox="0 0 22 22"><circle cx="11" cy="11" r="9.5" fill="none" stroke="currentColor" stroke-width="1.8"/><path d="M9 7l4 4-4 4" fill="none" stroke="currentColor" stroke-width="1.8"/></svg>
  </div>
</section>

<section class="services">
  <h2 class="abs">Transformation<br>Supported<br>by Technology</h2>
  <p class="abs services-intro">During our early years, Corvalin focused only on business transformation. We came to realize that successful transformation often depended on quality software implementations, and often more than one. Now we focus on five things, the five things most businesses need to reach their goals.</p>

  <div class="abs service" style="left:89px">
    <svg viewBox="0 0 40 50" width="40"><rect x="8" y="6" width="26" height="38" fill="none" stroke="#2e6da4" stroke-width="1.6"/><path d="M4 10v38h26" fill="none" stroke="#2e6da4" stroke-width="1.6"/><path d="M13 16h16M13 22h16M13 28h16M13 34h10" stroke="#2e6da4" stroke-width="1.6"/></svg>
    <h3>Business<br>Transformation</h3>
    <p>Define and execute<br>your strategee.</p>
    <span class="more">→</span>
  </div>
  <div class="abs service" style="left:289px">
    <svg viewBox="0 0 50 50" width="48"><rect x="4" y="8" width="40" height="30" fill="none" stroke="#2e6da4" stroke-width="1.6"/><rect x="12" y="14" width="14" height="12" fill="none" stroke="#2e6da4" stroke-width="1.6"/><path d="M30 16h9M30 22h9M16 44h16M24 38v6" stroke="#2e6da4" stroke-width="1.6"/></svg>
    <h3>ERP<br>Solutions</h3>
    <p>Assess, upgrade, and<br>implement ERP solutions<br>to meet your needs.</p>
    <span class="more">Read More →</span>
  </div>
  <div class="abs service" style="left:494px">
    <svg viewBox="0 0 50 50" width="50"><rect x="6" y="6" width="28" height="30" fill="none" stroke="#2e6da4" stroke-width="1.6"/><path d="M11 14h18M11 20h18M11 26h12M14 36v8h12v-8" fill="none" stroke="#2e6da4" stroke-width="1.6"/><circle cx="40" cy="30" r="6" fill="none" stroke="#2e6da4" stroke-width="1.6"/></svg>
    <h3>CRM<br>Solutions</h3>
    <p>Take your relationship<br>to the next level.</p>
    <span class="more">→</span>
  </div>
  <div class="abs service" style="left:699px">
    <svg viewBox="0 0 50 50" width="48"><rect x="3" y="6" width="42" height="30" fill="none" stroke="#2e6da4" stroke-width="1.6"/><path d="M10 30V22M15 30V16M20 30V20M20 44h10M25 36v8" stroke="#2e6da4" stroke-width="1.6"/><circle cx="34" cy="21" r="7" fill="none" stroke="#2e6da4" stroke-width="1.6"/><path d="M34 14v7h7" fill="none" stroke="#2e6da4" stroke-width="1.6"/></svg>
    <h3>Data and Business<br>Intelligence</h3>
    <p>Discover, connect, and<br>trust your data.</p>
    <span class="more">→</span>
  </div>
  <div class="abs service" style="left:904px">
    <span class="wordmark" style="height:50px;padding-top:16px">Elevate<small>By Corvalin</small></span>
    <h3>Building the Right<br>Team of People</h3>
    <p>Hire resources for your<br>transfromation journey.</p>
    <span class="more">→</span>
  </div>
</section>

<section class="people">
  <h2 class="abs">It’s the People</h2>
  <p class="abs people-intro">The world has changed in the past twenty years. The people you need might not all work for one company. Our clients want the best resources, available quickly. That’s why, in addition to our team of experts, we partner with:</p>
  <div class="abs point" style="left:99px;width:440px"><b>1</b><span>A large network of expert consultants<br>who are the best at what they do,</span></div>
  <div class="abs point" style="left:580px;width:520px"><b>2</b><span>Service providers all over the world to provide<br>the resources and value that are right for you,<br>available 24 x 7.</span></div>
  <div class="abs map" role="img" aria-label="Dotted world map with consultant portraits placed across continents"></div>
  <div class="abs pin" style="top:358px;left:186px" role="img" aria-label="Consultant portrait"></div>
  <div class="abs pin" style="top:363px;left:500px" role="img" aria-label="Consultant portrait"></div>
  <div class="abs tag">Leo R.</div>
  <div class="abs pin" style="top:359px;left:806px" role="img" aria-label="Consultant portrait"></div>
  <div class="abs pin" style="top:397px;left:924px" role="img" aria-label="Consultant portrait"></div>
  <div class="abs pin" style="top:473px;left:423px" role="img" aria-label="Consultant portrait"></div>
  <div class="abs pin" style="top:509px;left:689px" role="img" aria-label="Consultant portrait"></div>
  <div class="abs pin" style="top:670px;left:344px" role="img" aria-label="Consultant portrait"></div>
  <div class="abs pin" style="top:671px;left:845px" role="img" aria-label="Consultant portrait"></div>
  <p class="abs people-note">People are invariably at the center of our customer’s success. Find out how we can add our experts to yours.</p>
  <div class="abs team-btn">OUR TEAM</div>
</section>

<section class="testimonials" role="img" aria-label="Dimmed photo of business people in a meeting behind client testimonial">
  <p class="abs eyebrow">Clients Testimonials</p>
  <h2 class="abs">See What Our Clients Speak</h2>
  <div class="abs avatar" role="img" aria-label="Client portrait"></div>
  <p class="abs quote">Corvalin quickly moved us past talking about what needed to be done, to doing it. Development projects are never easy and when things got tough in the first phase of development, Corvalin stepped in to right the ship and put us on a new course.</p>
  <p class="abs author">MARA ELLISON, PRESIDENT<span>Brightline Controls</span></p>
  <div class="abs dots" style="top:472px;width:100%"><i></i><i class="on"></i><i></i></div>
</section>

<section class="tech">
  <p class="abs eyebrow">Technologies</p>
  <h2 class="abs">Rotator of Technologies</h2>
  <div class="abs logos">
    <span>Meridian Ledger</span><span>Orbitane</span><span>Funnelio</span><span>Quarry BI</span><span>Norvane Data</span><span>Plotvane</span>
  </div>
  <div class="abs tech-dots"><i></i><i class="on"></i><i></i><i></i></div>
</section>

<footer>
  <div class="abs brand">Corvalin</div>
  <p class="abs footer-about">We do more for our customers than implement software. We listen. We work to understand where they are in their transformation journey and where they want to go. We partner with them to clear the roadblocks that stand in their way, ensuring they reach their destination.</p>
  <div class="abs footer-col" style="left:614px">
    <h4>Address</h4>
    <p>418 Lakeview Plaza<br>Suite 210, Riverton, MN<br>55402</p>
    <div class="socials"><i aria-label="Professional network"></i><i aria-label="Search profile"></i></div>
  </div>
  <div class="abs footer-col" style="left:869px">
    <h4>Say Hello</h4>
    <span class="email">info@corvalinconsulting.com</span>
    <p class="phone">(555) 014-2290</p>
  </div>
  <p class="abs footer-links">Offerings &nbsp;|&nbsp; Capabilities &nbsp;|&nbsp; Industries &nbsp;|&nbsp; Team &nbsp;|&nbsp; About</p>
  <p class="abs copyright">© 2023 Corvalin Consulting. All Rights Reserved.</p>
</footer>

</body>
</html>
```